" Trata-se de uma construtora em conjunto com um escritório de engenharia e arquitetura para prestar serviços de construção, gerenciamento de obras e projetos e desenho. "

```html
<!DOCTYPE html>
<html lang="pt-BR">
<head>
<meta charset="utf-8">
<title>N7R — Construção e Engenharia</title>
<link href="https://fonts.googleapis.com/css2?family=Montserrat:wght@500;600;700&display=swap" rel="stylesheet">
<style>
  :root {
    --page-bg: #1f2630;
    --header-bg: #1d2836;
    --gold: #f2b41d;
    --nav-text: #e9e4d6;
    --white: #ffffff;
    --sky-top: #6e5a52;
    --sky-glow: #f0a13a;
    --sky-warm: #d9822f;
    --city-dark: #2d3442;
  }
  * { box-sizing: border-box; margin: 0; padding: 0; }
  html, body {
    width: 1200px; height: 1200px; overflow: hidden;
    background: var(--page-bg);
    font-family: "Montserrat", sans-serif;
  }
  .site {
    position: absolute; left: 0; top: 262px;
    width: 1200px; height: 675px;
    overflow: hidden;
  }
  .site-header {
    position: absolute; left: 0; top: 0; width: 100%; height: 78px;
    background: var(--header-bg);
    display: flex; align-items: center;
    padding: 0 42px;
    z-index: 2;
  }
  .brand {
    display: flex; align-items: center; gap: 10px;
    color: var(--gold); font-weight: 600; font-size: 20px; letter-spacing: 4px;
  }
  .brand-mark { width: 12px; height: 12px; background: var(--gold); }
  .main-nav {
    margin-left: auto; display: flex; gap: 22px;
    font-size: 15px; font-weight: 600; letter-spacing: 0.5px;
  }
  .main-nav a { color: var(--nav-text); text-decoration: none; }
  .main-nav a.is-active { color: var(--gold); }
  .social { display: flex; gap: 10px; margin-left: 60px; }
  .social span { width: 12px; height: 12px; border-radius: 50%; background: var(--gold); }
  .hero-photo {
    position: absolute; inset: 0;
    background:
      linear-gradient(180deg, rgba(29,40,54,0) 55%, rgba(45,52,66,0.85) 100%),
      radial-gradient(ellipse 60% 45% at 45% 40%, var(--sky-glow) 0%, var(--sky-warm) 40%, rgba(110,90,82,0) 80%),
      linear-gradient(180deg, var(--sky-top) 0%, #b7773c 45%, var(--city-dark) 100%);
  }
  .hero-copy {
    position: absolute; left: 0; top: 212px; width: 100%;
    text-align: center; color: var(--white);
    font-weight: 700; font-size: 52px; line-height: 66px;
    z-index: 1;
  }
  .hero-copy .accent { color: var(--gold); }
  .scroll-cue { position: absolute; left: 568px; top: 400px; z-index: 1; }
</style>
</head>
<body>
  <main class="site">
    <header class="site-header">
      <div class="brand"><span class="brand-mark"></span>N7R</div>
      <nav class="main-nav">
        <a class="is-active" href="#">HOME</a>
        <a href="#">QUEM SOMOS</a>
        <a href="#">SERVIÇOS</a>
        <a href="#">DEPOIMENTOS</a>
        <a href="#">FALE CONOSCO</a>
      </nav>
      <div class="social"><span></span><span></span><span></span></div>
    </header>
    <div class="hero-photo" role="img" aria-label="Foto de horizonte urbano com arranha-céus ao pôr do sol"></div>
    <h1 class="hero-copy">Construíndo <span class="accent">Sonhos</span><br>Administrando o futuro.</h1>
    <svg class="scroll-cue" width="64" height="64" viewBox="0 0 64 64" aria-label="Rolar para baixo">
      <circle cx="32" cy="32" r="30" fill="#ffffff"/>
      <path d="M32 16 V46 M20 34 L32 46 L44 34" fill="none" stroke="#2d3442" stroke-width="4" stroke-linecap="round" stroke-linejoin="round"/>
    </svg>
  </main>
</body>
</html>
```